Business Card Design Project

I require a business card with the following information on them for various different people;
name
m:
f:
e:
I have a logo already and will attached that. We are in the construction industry. I require something clean and simple but eye catching at the same time. You can use another colour with our logo if you like and you can style the logo as well if you wish. I am open.
Also it needs to be front and back design.
Industry/Entity Type
Construction
Requirements
Must have
- Logo, name, mobile, fax and email address.
Front and back design

```html
<!DOCTYPE html>
<html lang="en">
<head>
<meta charset="utf-8">
<title>Northfield Developments – Business Card</title>
<link href="https://fonts.googleapis.com/css2?family=Questrial&display=swap" rel="stylesheet">
<style>
  :root {
    --bg: #8a8a8a;
    --green-light: #a6dc3c;
    --green: #7cc225;
    --green-dark: #4f9a12;
    --brand-green: #6cb52a;
    --white: #ffffff;
    --panel-grey: #e6e6e6;
    --ink: #1c1c1c;
    --muted: #8d8d8d;
  }
  * { margin: 0; padding: 0; box-sizing: border-box; }
  html, body { width: 1200px; height: 900px; overflow: hidden; }
  body {
    background: var(--bg);
    font-family: "Questrial", "Century Gothic", sans-serif;
    display: flex;
    flex-direction: column;
    align-items: center;
    justify-content: center;
    gap: 56px;
  }
  .card {
    width: 620px;
    height: 380px;
    position: relative;
    overflow: hidden;
    background: var(--white);
  }

  /* Front */
  .card--front { display: flex; flex-direction: column; }
  .band { height: 28%; background: linear-gradient(180deg, var(--green-light), var(--green) 60%, var(--green-dark)); }
  .band--bottom { height: 26%; background: linear-gradient(180deg, var(--green-dark), var(--green) 45%, var(--green-light)); }
  .band-middle {
    flex: 1;
    background: linear-gradient(180deg, var(--white), var(--panel-grey));
    display: flex;
    align-items: center;
    justify-content: center;
  }

  .wordmark { display: flex; align-items: center; gap: 14px; }
  .wordmark__square { background: var(--brand-green); }
  .wordmark__name { color: var(--brand-green); white-space: nowrap; }
  .card--front .wordmark__square { width: 40px; height: 40px; }
  .card--front .wordmark__name { font-size: 36px; }

  /* Back */
  .card--back { padding: 46px 52px; }
  .card--back .wordmark { gap: 10px; margin-bottom: 30px; margin-left: 2px; }
  .card--back .wordmark__square { width: 24px; height: 24px; }
  .card--back .wordmark__name { font-size: 22px; }

  .person { font-size: 27px; color: var(--brand-green); margin-bottom: 22px; letter-spacing: 0.5px; }
  .person__role { font-size: 17px; color: var(--ink); margin-left: 4px; }

  .contact { list-style: none; font-size: 18px; color: var(--ink); line-height: 1.55; letter-spacing: 0.4px; }
</style>
</head>
<body>

  <section class="card card--front" aria-label="Card front">
    <div class="band"></div>
    <div class="band-middle">
      <div class="wordmark">
        <span class="wordmark__square"></span>
        <span class="wordmark__name">Northfield Developments</span>
      </div>
    </div>
    <div class="band band--bottom"></div>
  </section>

  <section class="card card--back" aria-label="Card back">
    <div class="wordmark">
      <span class="wordmark__square"></span>
      <span class="wordmark__name">Northfield Developments</span>
    </div>
    <p class="person">Daniel Harlow <span class="person__role">/ inventor</span></p>
    <ul class="contact">
      <li>M: PO Box 456 Ferndale, Victoria</li>
      <li>P : 02 9876 5432</li>
      <li>F : 02 9876 5432</li>
      <li>E : daniel.harlow@northfield.com.au</li>
    </ul>
  </section>

</body>
</html>
```